브랜드 소개
안녕하세요! ‘Walking beside you’ 당신과 동행하겠습니다.
저희는 음료브랜드 담솔라입니다.
담솔라는 2010년 8월 설립된 음료파우더 제조회사 누리벨의 온라인 브랜드로, 현재 식사대용음료를 비롯한 카페전용 파우더 등을 공급하는 음료브랜드입니다..
저희 담솔라가 이번에 출시할 신제품은 '곡물바람'입니다.
남녀노소 누구나 좋아하는 식사대용이자 간식 시리얼!
1. 시리얼은 우유가 있어야 먹을 수 있다.
2. 시리얼은 그릇과 숟가락이 필요하다.
3. 시리얼을 먹은 후에는 설거지를 해야한다.
4. 시리얼은 잘 밀봉해서 관리해야한다.
5. 시리얼은 정해진 정량대로 먹기 힘들다.
등등 시리얼의 틀에 박힌 고정관념을 탈피하고 소비자의 불편을 해소하며 만족을 높이는 '개성있고 스웩넘치는' 시리얼을 만들고 싶습니다.
간단히 설명드리자면 '곡물바람'은 우유없이 간편하게 물만 부어서 흔들어 마실 수 있는 시리얼입니다. 자세한 설명은 '펼침마당 디자인의뢰서 첨부파일'을 참고해주시기 바랍니다.

```html
<!DOCTYPE html>
<html lang="en">
<head>
<meta charset="utf-8">
<title>GRAIN BREEZE — Bottle Labels</title>
<link rel="stylesheet" href="https://fonts.googleapis.com/css2?family=Archivo+Black&family=Space+Mono:wght@700&display=swap">
<style>
  :root {
    --page: #f4f1ea;
    --ink: #1d1f3b;
    --white: #ffffff;
    --tag-red: #e6334a;
    --yogurt-base: #f7b21c;
    --yogurt-accent: #3cb7c9;
    --yogurt-deep: #8a5a3c;
    --berry-base: #3fc6c2;
    --berry-accent: #f39bb7;
    --berry-deep: #e4403f;
    --almond-base: #1f8a5a;
    --almond-accent: #e7437f;
    --almond-deep: #6a3b2a;
  }
  * { box-sizing: border-box; margin: 0; padding: 0; }
  html, body { width: 1200px; height: 1200px; overflow: hidden; }
  body {
    background: var(--page);
    display: flex;
    align-items: center;
    justify-content: center;
    gap: 48px;
  }
  .label {
    position: relative;
    width: 320px;
    height: 760px;
    border-radius: 40px;
    overflow: hidden;
  }
  .label__art {
    position: absolute;
    inset: 0;
  }
  .label--yogurt .label__art {
    background: linear-gradient(170deg, var(--yogurt-base) 0%, var(--yogurt-base) 55%, var(--yogurt-accent) 78%, var(--yogurt-deep) 100%);
  }
  .label--berry .label__art {
    background: linear-gradient(175deg, var(--berry-base) 0%, var(--berry-base) 52%, var(--berry-accent) 72%, var(--berry-deep) 100%);
  }
  .label--almond .label__art {
    background: linear-gradient(170deg, var(--almond-base) 0%, var(--almond-base) 50%, var(--almond-accent) 72%, var(--almond-deep) 100%);
  }
  .label__tagline {
    position: absolute;
    top: 150px;
    left: 0;
    right: 0;
    text-align: center;
    font-family: "Space Mono", monospace;
    font-size: 15px;
    line-height: 1.35;
    color: var(--white);
  }
  .label__badge {
    position: absolute;
    top: 228px;
    left: 20px;
    width: 280px;
    height: 280px;
    border-radius: 50%;
    background: var(--white);
    display: flex;
    flex-direction: column;
    align-items: center;
    justify-content: center;
    text-align: center;
  }
  .label__name {
    font-family: "Archivo Black", sans-serif;
    font-size: 44px;
    line-height: 1;
    color: var(--ink);
    letter-spacing: -1px;
  }
  .label__flavour {
    margin-top: 22px;
    font-family: "Space Mono", monospace;
    font-size: 13px;
    letter-spacing: 2px;
    line-height: 1.5;
    color: var(--ink);
  }
  .label__maker {
    position: absolute;
    bottom: 44px;
    left: 50%;
    transform: translateX(-50%);
    padding: 6px 14px;
    background: var(--tag-red);
    color: var(--white);
    font-family: "Space Mono", monospace;
    font-size: 13px;
    letter-spacing: 1px;
  }
</style>
</head>
<body>
  <section class="label label--yogurt">
    <div class="label__art" role="img" aria-label="Playful illustration of yogurt drops and granola pieces on yellow and teal shapes"></div>
    <p class="label__tagline">Get your GRAIN!<br>Get your BREEZE!</p>
    <div class="label__badge">
      <h2 class="label__name">GRAIN<br>BREEZE</h2>
      <p class="label__flavour">YOGURT<br>&amp; GRANOLA</p>
    </div>
    <span class="label__maker">DAMSOLA</span>
  </section>

  <section class="label label--berry">
    <div class="label__art" role="img" aria-label="Playful illustration of strawberries and a corn cob on teal and pink shapes"></div>
    <p class="label__tagline">Get your GRAIN!<br>Get your BREEZE!</p>
    <div class="label__badge">
      <h2 class="label__name">GRAIN<br>BREEZE</h2>
      <p class="label__flavour">STRAWBERRY<br>&amp; CORN</p>
    </div>
    <span class="label__maker">DAMSOLA</span>
  </section>

  <section class="label label--almond">
    <div class="label__art" role="img" aria-label="Playful illustration of almonds and chocolate pieces on green and pink shapes"></div>
    <p class="label__tagline">Get your GRAIN!<br>Get your BREEZE!</p>
    <div class="label__badge">
      <h2 class="label__name">GRAIN<br>BREEZE</h2>
      <p class="label__flavour">ALMOND<br>&amp; CHOCOLATE</p>
    </div>
    <span class="label__maker">DAMSOLA</span>
  </section>
</body>
</html>
```